Downloadable PDF "Brochure?"

We have a Free download we will provide in exchange for an email address on our new Trailmark website. The website at www.venturetrailmark-example.com is in development and will look nothing like what it currently does, but you can go there and get a sense of what Trailmark is from the text on the website. (see the attached image 'site design' for the new redesigned website for aesthetics).

We are looking for a nice design for the document, that will represent the mostly text document well. We are not actually looking to print these at a printer so they don't have to be print ready. I went ahead and included the logo and colors and fonts file again just for reference.

Target Market(s)

Business Owners / Decision Makers

Requirements
Must have
• See attached document 'trailmark freebie' for text to be utilized in the finished deliverable.
• See the attached image 'Site Design' for the website aesthetic.

```html
<!DOCTYPE html>
<html lang="en">
<head>
<meta charset="utf-8">
<title>Trailmark – 10 Questions To Choose The Best Technology Advisor</title>
<link rel="stylesheet" href="https://fonts.googleapis.com/css2?family=Cinzel:wght@400;700&family=Open+Sans:ital,wght@0,300;0,400;0,600;1,400&display=swap">
<style>
:root{
  --board:#c8c8c8;
  --slate:#2f3d44;
  --slate-dark:#253238;
  --rust:#c0683a;
  --rust-light:#d48458;
  --paper:#ffffff;
  --mist:#eef0f1;
  --ink:#2a2a2a;
  --label:#1d1d1d;
}
*{box-sizing:border-box;margin:0;padding:0}
html,body{width:922px;height:1200px;overflow:hidden;background:var(--board)}
body{position:relative;font-family:"Open Sans",Arial,sans-serif;color:var(--ink)}
.board-label{position:absolute;width:377px;text-align:center;font-weight:600;font-size:17px;color:var(--label);letter-spacing:.3px}
.page{position:absolute;width:377px;height:488px;background:var(--paper);overflow:hidden;box-shadow:0 1px 4px rgba(0,0,0,.25)}
.abs{position:absolute}
.footer-band{position:absolute;left:0;width:377px;height:24px;background:linear-gradient(90deg,var(--slate) 0%,var(--slate) 35%,var(--rust) 100%);display:flex;align-items:center;justify-content:center;font-family:"Cinzel",Georgia,serif;font-size:8.6px;color:#fff;letter-spacing:.3px}
.wordmark{display:flex;align-items:center;justify-content:center;gap:6px}
.wordmark-square{width:9px;height:9px;background:var(--slate)}
.wordmark-name{font-family:"Open Sans",Arial,sans-serif;font-weight:600;color:var(--slate);letter-spacing:2px}
.wordmark-line{font-family:"Open Sans",Arial,sans-serif;font-weight:400;color:var(--slate);text-align:center;letter-spacing:.4px}
.q{position:absolute}
.q-head{font-size:9.6px;line-height:12px;color:var(--rust)}
.q-icon{display:inline-block;width:9px;height:9px;background:var(--slate);color:#fff;font-size:6.5px;line-height:9px;text-align:center;font-family:"Cinzel",serif;font-weight:700;margin-right:5px;vertical-align:1px}
.q-rule{position:relative;height:1px;background:var(--slate);margin:3px 3px 0 auto}
.q-rule::after{content:"";position:absolute;right:-3px;top:-2.5px;width:5px;height:5px;border:1px solid var(--slate);border-radius:50%;background:var(--paper)}
.q-body{font-size:5.5px;line-height:8.5px;color:#333;margin-top:7px;text-align:justify}
.on-dark .q-head,.on-dark .q-body{color:#fff}
.on-dark .q-rule{background:#fff}
.on-dark .q-rule::after{border-color:#fff;background:var(--slate)}
.q-lead{margin-top:6px;color:#fff;font-weight:600;font-size:6.7px}
.photo{position:absolute}
</style>
</head>
<body>

<div class="board-label" style="left:83px;top:53px">COVER PAGE</div>
<div class="board-label" style="left:471px;top:53px">INNER PAGE 1</div>
<div class="board-label" style="left:83px;top:1117px">INNER PAGE 2</div>
<div class="board-label" style="left:471px;top:1117px">INNER PAGE 3</div>

<section class="page cover" style="left:83px;top:86px">
  <div class="photo" role="img" aria-label="Businessman standing at a large circular concrete window overlooking a city skyline" style="left:196px;top:0;width:181px;height:440px;background:linear-gradient(180deg,#b9bcbc 0%,#d5dbdd 30%,#9aa3a6 55%,#c9ccca 75%,#e3e4e2 100%)"></div>
  <div class="abs" style="left:0;top:0;width:203px;height:154px;background:var(--paper);border-bottom-right-radius:14px"></div>
  <div class="abs wordmark" style="left:0;top:94px;width:202px">
    <span class="wordmark-square"></span><span class="wordmark-name" style="font-size:15px">TRAILMARK</span>
  </div>
  <div class="abs wordmark-line" style="left:0;top:118px;width:202px;font-size:7px">Clear Thinking For Growing Firms</div>
  <div class="abs" style="left:0;top:154px;width:222px;height:132px;background:linear-gradient(90deg,var(--slate) 0%,var(--slate) 88%,var(--rust) 88%,var(--rust) 100%);border-top-right-radius:12px;border-bottom-right-radius:12px"></div>
  <div class="abs" style="left:0;top:170px;width:202px;text-align:center;color:#fff;font-weight:300;font-size:12.5px;line-height:16px">10 Questions To<br>Choose The Best</div>
  <div class="abs" style="left:36px;top:207px;width:128px;height:1px;background:#fff;opacity:.8"></div>
  <div class="abs" style="left:0;top:214px;width:202px;text-align:center;color:#fff;font-family:'Cinzel',Georgia,serif;font-size:22px;line-height:23px">TECHNOLOGY</div>
  <div class="abs" style="left:0;top:234px;width:202px;text-align:center;color:#fff;font-family:'Cinzel',Georgia,serif;font-size:32px;line-height:34px">ADVISOR</div>
  <div class="abs" style="left:0;top:286px;width:202px;height:148px;background:linear-gradient(180deg,var(--paper),var(--mist))"></div>
  <p class="abs" style="left:22px;top:306px;width:160px;text-align:center;font-style:italic;font-size:6.2px;line-height:9.3px;color:#333">When you choose a technology advisor whether it be a Managed Service Provider, fractional CIO or a full-time CIO you need to make sure that they understand business just as much as they understand technology. Some of the biggest complaints about the IT department are that they just don’t “Get it”. The questions below should help you determine whether or not they have a technology mindset or a business mindset.</p>
  <div class="footer-band" style="top:433px;height:42px">WWW.VENTURETRAILMARK-EXAMPLE.COM</div>
</section>

<section class="page inner-one" style="left:471px;top:86px">
  <div class="q" style="left:27px;top:26px;width:326px">
    <p class="q-head"><span class="q-icon">Q</span>What is scalability? How important is it from a technology perspective on a scale of 1-&gt;10 with 10 being the highest? What all does scalability impact?</p>
    <div class="q-rule" style="width:45%"></div>
    <p class="q-body">This question is designed to get a reading on the person’s mindset. A typical technology-minded response would be something describing the ability of systems or software to scale by adding additional resources. When working from a business point of view, however, you want to see it defined as the ability for the organization to support increased volume without sacrificing margins. The importance of this concept cannot be overstated and should be a 9 or 10 in terms of ranking. Regarding impact, you want to see not just an understanding of having to spend money two or three times for a different solution to the same problem, but an acknowledgment of the ‘total’ cost, including adoption fatigue, the opportunity cost of change, and the competitive disadvantage it creates. For concepts of business scalability refer to ‘Growing Wide’ by Dale Porter.</p>
  </div>
  <div class="q" style="left:27px;top:160px;width:326px">
    <p class="q-head"><span class="q-icon">Q</span>Provide an example where you solved a problem without the use of technology.</p>
    <div class="q-rule" style="width:60%"></div>
    <p class="q-body">Often technology-minded individuals become so wrapped up in the solutions themselves they fail to realize a policy or process change is far more effective and simple than making changes to existing or introducing new technology. Asking for a specific example here should demonstrate the ability to think from a business mindset. For specific examples reference ‘The Ember Initiative’ by Ross, Lindqvist, and Mead.</p>
  </div>
  <div class="q" style="left:27px;top:250px;width:326px">
    <p class="q-head"><span class="q-icon">Q</span>How do you go about prioritizing solutions in order of importance for implementation / adoption?</p>
    <div class="q-rule" style="width:50%"></div>
    <p class="q-body">Answers here should include reference to some form of discovery process or a thorough evaluation at the operations level. One of the key skill sets for someone approaching technology from a business point of view is mapping solutions and their respective importance to business outcomes and (often more importantly) eliminating bottlenecks while respecting that some implementations must necessarily come before others to be viable. For reference on the Theory of Constraints see ‘The Aim’ by Aron Keller.</p>
  </div>
  <div class="q" style="left:27px;top:344px;width:326px">
    <p class="q-head"><span class="q-icon">Q</span>What is Information Technology Debt?</p>
    <div class="q-rule" style="width:36%;margin-top:-7px"></div>
    <p class="q-body" style="margin-top:9px">Stated simply, ‘IT Debt’ is a measurement of the out-of-date, incomplete or yet-to-be-defined technology changes. Debt occurs for a number of reasons, including lack of qualified personnel to implement the needed solutions (or recognize the problem in the first place); historical spending haunting the organization “we spent money on something like this before and look what it got us”; Fire-fighting (addressing issues purely reactively in a downward spiral leaving no time for fixing the real underlying problem); or most commonly, the budget being already allocated to other company endeavors that seem immediately more pressing. By recognizing what IT Debt is, the individual demonstrates an acknowledgment of how impactful it can be when neglected and not brought to the forefront of business planning sessions.</p>
  </div>
  <div class="footer-band" style="top:453px">WWW.VENTURETRAILMARK-EXAMPLE.COM</div>
</section>

<section class="page inner-two" style="left:83px;top:603px">
  <div class="q" style="left:27px;top:26px;width:326px">
    <p class="q-head"><span class="q-icon">Q</span>Provide an example where you argued against implementing a technology solution and why.</p>
    <div class="q-rule" style="width:55%"></div>
    <p class="q-body">Despite it being seemingly obvious, using ‘outside of budget’ is not a good answer. Business-minded technology advisors should be intimately aware of how well a proposed solution will integrate into the existing company ecosystem (software tools already present, workflow, and processes), if it drives the company toward reducing/eliminating a bottleneck (and thereby creates more leverage), and if it fits the company’s culture. If any of these are a no, the solution should be carefully examined for what it really offers the organization. If yes, the budget should be evaluated as a cost-benefit analysis, not a flat number ‘not to exceed’.</p>
  </div>
  <div class="q" style="left:27px;top:133px;width:326px">
    <p class="q-head"><span class="q-icon">Q</span>What is your ideal method for maintaining technology alignment for the company?</p>
    <div class="q-rule" style="width:55%"></div>
    <p class="q-body">You want to see a specific process envisioned here. At the very least a recommendation to be involved in business planning meetings or retreats, and ideally a standing technology focused meeting with leadership present should be argued for. For technology to be truly in alignment, it must fit the needs of the organization, not the other way around. This needs to come from the top level, and it means a representative must be present in critical business strategy meetings to understand where the company is headed, what operational constraints they are encountering, and what their short-term goals are. For an outline of how this model has been the underlying key to success for several well-known companies reference ‘Steady to Strong’ by Paul Hendry.</p>
  </div>
  <div class="abs" style="left:0;top:246px;width:377px;height:230px;background:linear-gradient(135deg,var(--slate) 0%,var(--slate-dark) 100%)"></div>
  <div class="photo" role="img" aria-label="Businessman with a briefcase facing a white maze" style="left:225px;top:246px;width:128px;height:193px;background:linear-gradient(180deg,#dfe3e5 0%,#c9cfd2 45%,#eef0f1 100%)"></div>
  <div class="q on-dark" style="left:27px;top:260px;width:190px">
    <p class="q-head" style="font-weight:600;font-size:10px"><span class="q-icon" style="background:var(--rust)">Q</span>How do you plan on measuring and monitoring the adoption success of a solution or project?</p>
    <div class="q-rule" style="width:45%"></div>
    <p class="q-body" style="font-size:5.7px;line-height:9.4px">Technically minded individuals often look at the point of ‘it’s up and running and it all works’, as where their responsibilities end. Someone with a business mindset should demonstrate that evaluating how well the solution has been adopted into the day to day workflow, and to what degree the solution has increased leverage or operational transparency are the true critical indicators of success. There should be a specific process of follow-up after implementation to flag adoption or workflow issues due to problems such as inadequate training, unforeseen incompatibilities (whether they be process or technology related), or simply resistance to change. These findings can then be brought back to leadership to evaluate how best to improve successful adoption going forward.</p>
  </div>
  <div class="footer-band" style="top:451px;background:linear-gradient(90deg,var(--slate) 0%,var(--rust) 50%,var(--slate) 100%)">WWW.VENTURETRAILMARK-EXAMPLE.COM</div>
</section>

<section class="page inner-three" style="left:471px;top:603px;background:var(--slate)">
  <div class="abs" style="left:157px;top:0;width:220px;height:131px;background:linear-gradient(135deg,var(--rust) 0%,var(--rust-light) 60%,var(--rust) 100%)"></div>
  <div class="abs" style="left:195px;top:38px;width:150px;text-align:center;color:#fff;font-size:10.2px;line-height:12.6px">Provide an example where you had to balance customer and employee technology experience with security and compliance.</div>
  <div class="abs" style="left:196px;top:106px;width:148px;height:1px;background:#fff"></div>
  <div class="abs" style="left:175px;top:131px;width:202px;height:306px;background:linear-gradient(180deg,var(--paper),var(--mist))"></div>
  <p class="abs" style="left:196px;top:147px;width:160px;text-align:justify;font-style:italic;font-size:5.8px;line-height:9.3px;color:#333">A critical role fulfilled by a technology advisor is being able to balance maintaining compliance and sound security practices with as painless of a technology experience as possible. They should be able to weigh the critical importance of protecting the organization from the negative public relations and liability of a security flaw while respecting a solution must be usable to be useful. Look for an example that demonstrates an understanding of both sides and strikes a balance without going to an extreme in either direction.</p>
  <div class="abs wordmark" style="left:175px;top:318px;width:202px">
    <span class="wordmark-square"></span><span class="wordmark-name" style="font-size:14px">TRAILMARK</span>
  </div>
  <div class="abs wordmark-line" style="left:175px;top:341px;width:202px;font-size:6.6px">Clear Thinking For Growing Firms</div>
  <div class="abs" style="left:231px;top:362px;width:86px;height:14px;border-radius:7px;background:var(--rust);color:#fff;font-family:'Cinzel',Georgia,serif;font-size:8px;line-height:14px;text-align:center">CONTACT US</div>
  <p class="abs" style="left:175px;top:382px;width:202px;text-align:center;font-weight:600;font-size:5.8px;line-height:9.2px;color:var(--slate)">1420 Harbor Ridge Parkway South,<br>Suite 300 Lakemont, TX 75010<br>hello@venturetrailmark-example.com<br>(555) 014-2290</p>
  <div class="q on-dark" style="left:26px;top:22px;width:120px">
    <div style="text-align:center"><span class="q-icon" style="background:var(--rust);margin:0">Q</span></div>
    <p class="q-lead" style="line-height:11px">What would you do first, if you were selected as our advisor? Can you give me details on what your discovery or on-boarding process includes?</p>
    <div class="q-rule" style="width:40%"></div>
    <p class="q-body" style="margin-top:9px;font-size:5.6px;line-height:10px">You are looking to make sure that they don’t stop at the technology. There should be a higher focus on understanding what the company processes are and how the people inside the organization get work done. If they focus only on network, security, and disaster recovery assessments then they do not have a business mindset.</p>
  </div>
  <div class="q on-dark" style="left:26px;top:208px;width:120px">
    <div style="text-align:center"><span class="q-icon" style="background:var(--rust);margin:0">Q</span></div>
    <p class="q-lead" style="line-height:10.5px">Can you give me an example of a time you gave a suggestion for a solution and it was not taken? Describe the solution and why it was important to the organization. And why do you think they didn’t implement it?</p>
    <div class="q-rule" style="width:40%"></div>
    <p class="q-body" style="margin-top:9px;font-size:5.6px;line-height:9.5px">When they describe why they think the solution was important do they simply talk about risk reduction or uptime improvements without tying them back to an organizational goal or bottleneck. Being able to demonstrate actual business value is a critical skill for a technology advisor. For reference on technical excellence in service of business objectives rather than blindly servicing requirements see ‘A Chair in The Room’ by Lena Ortiz.</p>
  </div>
  <div class="footer-band" style="top:434px;height:26px;background:linear-gradient(90deg,var(--slate) 0%,var(--rust) 45%,var(--rust) 100%)">WWW.VENTURETRAILMARK-EXAMPLE.COM</div>
  <div class="abs" style="left:220px;top:470px;width:157px;height:18px;background:var(--paper);border-top-left-radius:30px 18px"></div>
</section>

</body>
</html>
```